New Packaging and label for New Beard Oil and Shampoo brand from London

Oils, Shampoo ect .. Beard Oil Ingredients: Application Directions: Apply to beard by weight in a small amount of oil will naturally absorb. Leaving it soft & conditioned. Ingredients: Coconut oil, scented oil, Oud oil, vitamin E 100% Natural `i will have 5 types of oils Vanilla Oud Rose Oud Cocktail Tea tree Arabian Night

Target Market(s)

A fashionable well groomed professional gentleman who is willing to invest in his appearance.

Industry/Entity Type

It Company

Font styles to use
Sans Serif

Colors

Designer to choose colors to be used in the design.

Requirements
Must have
• Beard Oil Ingredients: Application Directions: Apply to a beard by a small amount of oil will naturally absorb. Leaving it soft & conditioned. Ingredients: Coconut Oil, Scented Oil, Oil Oud, Vitamin E 100% Natural 1.0z 30ml Made in Uk i will have 5 types of oils Vanilla Oud Rose Oud Cocktail Tea Tree Arabian Beard Night Shampoo APPLICATION DIRECTIONS Massage into the beard / hair and rinse out with warm water. Distorted shampoos, there are no nasty chemicals which are damaging your beard instead of the wheat proteins and oils that you add to the hair follicles with nutrients and naturally adding a protective coating. INGREDIENTS Aqua (Water), Capryl / caprylyl glucoside, Cocomidopropyl betaine, Glycerin (Veg), Xanthan gum, Phenoxyethanol, Hydrolysed wheat protein, Aloe barbadensis (Aloe vera) leaf powder, Sodium benzoate, Potassium sorbate1 3.4 oz, 100ml Cylinder packaging for the Oils, Box for the shampoo
Nice to have
• I want "London" written underneath the logo and oil name.

```html
<!DOCTYPE html>
<html lang="en">
<head>
<meta charset="utf-8">
<title>Noble Whisker — Beard Oil Label</title>
<link href="https://fonts.googleapis.com/css2?family=Barlow:wght@400;500;600;700&family=Barlow+Semi+Condensed:wght@500;700&family=Kaushan+Script&display=swap" rel="stylesheet">
<style>
  :root {
    --backdrop: #dfb8bc;
    --label: #ffffff;
    --ink: #2b2b2b;
    --gold: #c9a44a;
    --gold-soft: #e2cd93;
    --bridge: #8a8a8a;
    --beard-dark: #4a4a4a;
    --beard-light: #bdbdbd;
  }
  * { box-sizing: border-box; margin: 0; padding: 0; }
  html, body { width: 1200px; height: 1162px; overflow: hidden; }
  body {
    background: var(--backdrop);
    font-family: "Barlow", sans-serif;
    position: relative;
  }
  .label {
    position: absolute;
    left: 300px; top: 131px;
    width: 600px; height: 900px;
    background: var(--label);
  }
  .label-lines { position: absolute; inset: 0; width: 600px; height: 900px; }
  .brand-name {
    position: absolute; top: 62px; left: 0; width: 100%;
    text-align: center;
    font-family: "Barlow Semi Condensed", sans-serif;
    font-weight: 700; font-size: 40px; letter-spacing: 1px;
    color: var(--ink);
  }
  .city {
    position: absolute; top: 168px; left: 0; width: 100%;
    text-align: center;
    font-weight: 500; font-size: 26px; letter-spacing: 2px;
    color: var(--gold);
  }
  .bridge-art {
    position: absolute; top: 228px; left: 205px;
    width: 190px; height: 76px;
    background: linear-gradient(180deg, #b9b9b9, var(--bridge));
  }
  .claim {
    position: absolute; top: 270px;
    font-weight: 600; font-size: 15px; letter-spacing: 1px;
    color: var(--ink); white-space: nowrap;
  }
  .claim--natural { left: 100px; transform: rotate(-50deg); transform-origin: left top; top: 372px; }
  .claim--volume { left: 418px; transform: rotate(50deg); transform-origin: left top; top: 262px; }
  .product-type {
    position: absolute; top: 368px; left: 0; width: 100%;
    text-align: center;
    font-family: "Barlow Semi Condensed", sans-serif;
    font-weight: 700; font-size: 76px; line-height: 0.92;
    color: var(--ink);
  }
  .beard-art {
    position: absolute; top: 520px; left: 125px;
    width: 350px; height: 260px;
    border-radius: 40% 40% 50% 50% / 30% 30% 70% 70%;
    background: radial-gradient(ellipse at 50% 35%, var(--beard-light), var(--beard-dark));
  }
  .scent {
    position: absolute; top: 752px; left: 0; width: 100%;
    text-align: center;
    font-family: "Kaushan Script", cursive;
    font-size: 66px; color: var(--ink);
    transform: rotate(-4deg);
  }
</style>
</head>
<body>
  <main class="label">
    <svg class="label-lines" viewBox="0 0 600 900" aria-hidden="true">
      <g stroke="var(--gold)" stroke-width="3">
        <line x1="0" y1="94" x2="150" y2="94"/>
        <line x1="0" y1="104" x2="150" y2="104" stroke="var(--gold-soft)"/>
        <line x1="450" y1="94" x2="600" y2="94"/>
        <line x1="450" y1="104" x2="600" y2="104" stroke="var(--gold-soft)"/>
      </g>
      <g fill="none" stroke="var(--gold)" stroke-width="4">
        <polyline points="222,286 108,400 190,482"/>
        <polyline points="378,286 492,400 410,482"/>
      </g>
      <g stroke="var(--gold)" stroke-width="2.5" fill="none">
        <line x1="62" y1="780" x2="128" y2="752"/>
        <line x1="52" y1="800" x2="118" y2="776"/>
        <line x1="480" y1="752" x2="548" y2="780"/>
        <line x1="488" y1="776" x2="555" y2="800"/>
        <path d="M150 862 Q300 880 450 850"/>
      </g>
    </svg>

    <div class="brand-name">NOBLE WHISKER</div>
    <div class="city">LONDON</div>
    <div class="bridge-art" role="img" aria-label="Line drawing of a London bridge skyline"></div>
    <div class="claim claim--natural">100% NATURAL</div>
    <div class="claim claim--volume">1 OZ · 30 ML</div>
    <h1 class="product-type">BEARD<br>OIL</h1>
    <div class="beard-art" role="img" aria-label="Hand-drawn illustration of a full beard and moustache"></div>
    <div class="scent">Vanilla Oud</div>
  </main>
</body>
</html>
```